Garage Flooring Flyer

We are looking for a flyer design for our garage flooring company. We specialise in installing garage floor coatings. We use industrial grade products and are serious about durability and quality.
We target male car enthusiasts and want to project the image of a modern high-tech company. The flyer should be stunningly visual and incorporate the logo and photos we have attached. Other photos or images are welcomed.
Some key mentions to be made on the flyer are listed below:
About Us
"We are K*** R***** LLC, Home of the garage enthusiasts and Waukesha’s premier garage floor installer"
Services
Garage Floor Coatings
Offers
-Call or Email for a FREE estimate!
Credentials
-QN logo
-Pictavo Logo
-Zorbin Logo
-5stars?
Benefit Highlights to be mentioned or listed (not in any particular order)
-Industrial Quality and Strength
-Easy to Clean
-Many Color Options
-Locally Owned and Operated
-Satisfaction Guaranteed
-Lifetime Limited Warranty
-Increases Home Value
-MAKE YOUR FRIENDS AND NEIGHBORS JEALOUS!
-Fully Insured
-Certified and Trusted Installer
-Oil and Chemical Resistant
-UV Stable
-Impact and Abrasion Resistant
Contact Info
-Phone
-Email
-Website
Captions
-"From diamond grinding surface prep to using only the highest industrial-grade products, we believe in taking the time to ensure a proper installation and guarantee a durable long-lasting and beautiful garage floor";
-Serving Southeastern Wisconsin!

```html
<!DOCTYPE html>
<html lang="en">
<head>
<meta charset="utf-8">
<title>Torvane Garage – Garage Floor Coatings Flyer</title>
<link href="https://fonts.googleapis.com/css2?family=Poppins:wght@400;500;600;700;800&display=swap" rel="stylesheet">
<style>
  :root{
    --page-bg:#e7e8e9;
    --paper:#ffffff;
    --brown:#7a4317;
    --brown-dark:#5e3210;
    --ink:#3b3b3b;
    --white:#ffffff;
  }
  *{box-sizing:border-box;margin:0;padding:0}
  html,body{width:1200px;height:1200px;overflow:hidden;background:var(--page-bg);font-family:"Poppins",sans-serif}
  .flyer{position:absolute;left:198px;top:32px;width:804px;height:1138px;background:var(--paper);box-shadow:6px 8px 14px rgba(0,0,0,.18);overflow:hidden}

  .hero-photo{position:absolute;left:0;top:60px;width:804px;height:352px;
    background:linear-gradient(180deg,#d9d3c8 0%,#bcb4a8 38%,#1d1c1e 50%,#151417 62%,#9e9890 75%,#c9c4bc 100%)}

  .brand{position:absolute;left:0;top:0;width:258px;height:84px;background:var(--paper);
    clip-path:polygon(0 0,100% 0,78% 100%,0 100%);display:flex;align-items:center;padding-left:40px}
  .brand-name{font-weight:700;font-size:16px;color:#1e1e1e;letter-spacing:.6px;line-height:1;white-space:nowrap}
  .title-bar{position:absolute;left:234px;top:0;width:570px;height:70px;background:var(--brown);
    clip-path:polygon(0 0,100% 0,100% 100%,5% 100%);display:flex;align-items:center;justify-content:center;padding-left:30px}
  .title-bar h1{color:var(--white);font-weight:600;font-size:32px;letter-spacing:.2px}

  .estimate-badge{position:absolute;left:658px;top:296px;width:124px;height:124px;border-radius:50%;
    background:var(--brown);border:3px solid var(--white);color:var(--white);text-align:center;
    display:flex;flex-direction:column;justify-content:center;font-weight:600;font-size:15px;line-height:1.1}
  .estimate-badge strong{font-size:21px;font-weight:700}

  .about-band{position:absolute;left:0;top:412px;width:804px;height:84px;background:var(--brown);
    color:var(--white);text-align:center;font-weight:600;font-size:22.5px;line-height:1.3;padding-top:8px}

  .swatch{position:absolute;top:496px;width:252px;height:176px;background:var(--paper);padding:10px}
  .swatch span{display:block;width:100%;height:100%}
  .swatch-1{left:12px}.swatch-2{left:276px}.swatch-3{left:540px}
  .swatch-1 span{background:linear-gradient(135deg,#5c5548,#2b2924 50%,#8c8273)}
  .swatch-2 span{background:linear-gradient(135deg,#b9b8b6,#8a8986 50%,#d8d7d3)}
  .swatch-3 span{background:linear-gradient(135deg,#5a5d60,#3a3c3f 50%,#7b7e80)}

  .benefits{position:absolute;left:40px;top:694px;width:430px}
  .benefits h2{width:250px;text-align:center;color:var(--brown);font-weight:700;font-size:20px;line-height:1.3;margin-bottom:14px}
  .benefits ul{list-style:none}
  .benefits li{font-size:16px;color:var(--ink);line-height:22.8px;padding-left:16px;position:relative}
  .benefits li::before{content:"";position:absolute;left:1px;top:8px;width:4px;height:8px;border:solid var(--brown);border-width:0 2px 2px 0;transform:rotate(40deg)}

  .testimonial{position:absolute;left:472px;top:730px;width:272px;height:258px;border:1.5px solid var(--brown);border-radius:14px;padding:28px 14px 0 18px}
  .testimonial p{font-size:16px;line-height:20px;color:var(--ink)}
  .testimonial p + p{margin-top:20px}
  .quote-mark{position:absolute;font-size:48px;font-weight:800;color:var(--brown);background:var(--paper);line-height:.9;height:26px;padding:0 3px;overflow:hidden}
  .quote-open{left:-10px;top:-12px}
  .quote-close{right:-10px;bottom:-14px}

  .social{position:absolute;right:36px;top:1052px;display:flex;gap:12px}
  .social-item{display:flex;align-items:center;gap:4px;font-size:14px;font-weight:600;color:var(--brown)}
  .social-item i{width:12px;height:12px;border-radius:50%;background:var(--brown)}

  .contact-bar{position:absolute;left:0;bottom:0;width:804px;height:46px;background:var(--brown);color:var(--white);
    display:flex;align-items:center;justify-content:center;gap:10px;font-size:16px}
  .contact-bar svg{width:16px;height:16px;fill:none;stroke:var(--white);stroke-width:1.8;vertical-align:-2px;margin-right:6px}
  .divider{opacity:.9}
</style>
</head>
<body>
<main class="flyer">
  <div class="hero-photo" role="img" aria-label="Black sports car parked on a glossy speckled flake-coated garage floor"></div>

  <div class="brand"><span class="brand-name">TORVANE GARAGE</span></div>
  <header class="title-bar"><h1>Garage Floor Coatings</h1></header>

  <div class="estimate-badge"><span>Call or Email<br>for a</span><strong>FREE</strong><span>estimate!</span></div>

  <section class="about-band">"We are K*** R***** LLC, Home of the garage enthusiasts<br>and Waukesha’s premier garage floor installer"</section>

  <div class="swatch swatch-1"><span role="img" aria-label="Dark brown and black flake floor sample"></span></div>
  <div class="swatch swatch-2"><span role="img" aria-label="Light grey and white flake floor sample"></span></div>
  <div class="swatch swatch-3"><span role="img" aria-label="Charcoal grey flake floor sample"></span></div>

  <section class="benefits">
    <h2>WE HAVE YOUR FLOORING COVERED</h2>
    <ul>
      <li>Industrial Quality and Strength</li>
      <li>Easy to Clean</li>
      <li>Many Color Options</li>
      <li>Locally Owned and Operated</li>
      <li>Satisfaction Guaranteed</li>
      <li>Lifetime Limited Warranty</li>
      <li>Satisfaction Guaranteed</li>
      <li>Increases Home Value</li>
      <li>MAKE YOUR FRIENDS AND NEIGHBORS JEALOUS!</li>
      <li>Fully Insured</li>
      <li>Certified and Trusted Installer</li>
      <li>Oil and Chemical Resistant</li>
      <li>UV Stable - Won't yellow</li>
      <li>Impact and Abrasion Resistant</li>
    </ul>
  </section>

  <blockquote class="testimonial">
    <span class="quote-mark quote-open">“</span>
    <p>From diamond grinding surface prep to using only the highest industrial-grade products, we believe in taking the time to ensure a proper installation and guarantee a durable long-lasting and beautiful garage floor</p>
    <p>Serving Southeastern Wisconsin!</p>
    <span class="quote-mark quote-close">”</span>
  </blockquote>

  <div class="social">
    <span class="social-item"><i></i>QN</span>
    <span class="social-item"><i></i>Pictavo</span>
    <span class="social-item"><i></i>Zorbin</span>
  </div>

  <footer class="contact-bar">
    <span><svg viewBox="0 0 24 24"><path d="M5 3h4l2 5-3 2a12 12 0 0 0 6 6l2-3 5 2v4a2 2 0 0 1-2 2A18 18 0 0 1 3 5a2 2 0 0 1 2-2z"/></svg>123-456-7890</span>
    <span class="divider">|</span>
    <span><svg viewBox="0 0 24 24"><rect x="3" y="5" width="18" height="14"/><path d="M3 5l9 8 9-8"/></svg>xyz@mailora.com</span>
    <span class="divider">|</span>
    <span><svg viewBox="0 0 24 24"><circle cx="12" cy="12" r="9"/><path d="M3 12h18M12 3c3 3 3 15 0 18M12 3c-3 3-3 15 0 18"/></svg>www.torvanegarage.com</span>
  </footer>
</main>
</body>
</html>
```